Dunmore IT Services needs to look professional and modern

This is my first time using this site so I am unsure what to expect, I am very serious in needing design work done and have no issues paying for it. I am hoping for good things as my business needs this before I can make any money !
Dunmore IT Services Pty Ltd core business is small / medium business networking, support and related hardware ie servers, PC's, Laptops, network equipment/infrastructure, printers etc
The focus of the business to give our customers a competitive edge over others by using new and innovative technologies and services. This is always balanced against stability, reliability and efficiency of the customers IT network.
We are looking for the design of a logo and business cards (there is also the potential for a website once this project is successfully completed). The design should have a sense of refinement and stability while being modern. The choice of colour pallet is up to the designer but nothing gordy.
The cards need to be double sided with the reverse to include brief points of business offered, details of points to be filled in by me later.
The front needs to include business name, mobile number (0471 392 508), my name (Rob Dunmore), email address (rob@DunmoreITServices.com.au), website address (www.DunmoreITServices.com.au), business slogan ("Your Competitive Edge")
Business
"Your Competitive Edge"
Designer to choose colors to be used in the design.

```html
<!DOCTYPE html>
<html lang="en">
<head>
<meta charset="utf-8">
<title>Dunmore IT Services – Business Cards</title>
<link rel="stylesheet" href="https://fonts.googleapis.com/css2?family=Questrial&display=swap">
<style>
  :root {
    --charcoal: #2f3439;
    --green: #8cc04b;
    --white: #ffffff;
    --paper: #ffffff;
    --edge: #262a2e;
  }
  * { margin: 0; padding: 0; box-sizing: border-box; }
  html, body {
    width: 1200px;
    height: 998px;
    overflow: hidden;
    background: var(--paper);
    font-family: "Questrial", "Century Gothic", sans-serif;
  }
  .canvas { position: relative; width: 1200px; height: 998px; }

  /* Business name lockup: plain square + name in one colour and weight */
  .brand { position: absolute; display: flex; align-items: center; white-space: nowrap; }
  .brand__square { flex: none; }
  .brand__name { line-height: 1; }

  .brand--page { right: 70px; top: 80px; gap: 12px; }
  .brand--page .brand__square { width: 16px; height: 16px; background: var(--charcoal); }
  .brand--page .brand__name { font-size: 26px; color: var(--charcoal); }

  /* Cards */
  .card {
    position: absolute;
    background: var(--charcoal);
    color: var(--white);
    border: 1px solid var(--edge);
  }
  .card--back { left: 161px; top: 161px; width: 518px; height: 298px; }
  .card--front {
    left: 316px; top: 438px; width: 729px; height: 419px;
    box-shadow: 0 -12px 24px -14px rgba(0,0,0,0.35);
  }

  .card--back .brand { left: 86px; top: 131px; gap: 14px; }
  .card--back .brand__square { width: 20px; height: 20px; background: var(--green); }
  .card--back .brand__name { font-size: 33px; color: var(--white); }

  .card--front .brand { right: 52px; top: 64px; gap: 10px; }
  .card--front .brand__square { width: 14px; height: 14px; background: var(--green); }
  .card--front .brand__name { font-size: 22px; color: var(--white); }

  .details { position: absolute; left: 50px; top: 58px; }
  .slogan { font-size: 27px; color: var(--green); line-height: 1; }
  .services { list-style: none; margin-top: 22px; font-size: 25px; }
  .services__row { display: flex; height: 37px; align-items: center; }
  .services__item::before {
    content: "•"; color: var(--green); font-size: 16px;
    margin: 0 8px 0 0; position: relative; top: -2px;
  }
  .services__item + .services__item { margin-left: 10px; }
  .person { font-size: 28px; color: var(--green); margin-top: 30px; line-height: 1; }
  .contacts { list-style: none; margin-top: 22px; font-size: 24px; }
  .contacts li { display: flex; align-items: center; height: 37px; }
  .contact__icon {
    width: 26px; height: 26px; border-radius: 50%;
    border: 2px solid var(--green);
    display: flex; align-items: center; justify-content: center;
    font-size: 17px; line-height: 1; margin-right: 12px; padding-bottom: 2px;
  }
</style>
</head>
<body>
<main class="canvas">

  <div class="brand brand--page">
    <span class="brand__square"></span>
    <span class="brand__name">Dunmore IT Services</span>
  </div>

  <section class="card card--back" aria-label="Card back">
    <div class="brand">
      <span class="brand__square"></span>
      <span class="brand__name">Dunmore IT Services</span>
    </div>
  </section>

  <section class="card card--front" aria-label="Card front">
    <div class="brand">
      <span class="brand__square"></span>
      <span class="brand__name">Dunmore IT Services</span>
    </div>

    <div class="details">
      <p class="slogan">Your competitive edge!</p>
      <ul class="services">
        <li class="services__row">
          <span class="services__item">networking</span>
          <span class="services__item">printers</span>
          <span class="services__item">systems</span>
        </li>
        <li class="services__row">
          <span class="services__item">laptops</span>
          <span class="services__item">PC’s</span>
          <span class="services__item">equipment</span>
        </li>
      </ul>
      <p class="person">Rob Dunmore</p>
      <ul class="contacts">
        <li><span class="contact__icon">p</span>0471 392 508</li>
        <li><span class="contact__icon">e</span>rob@DunmoreITServices.com.au</li>
        <li><span class="contact__icon">w</span>DunmoreITServices.com.au</li>
      </ul>
    </div>
  </section>

</main>
</body>
</html>
```